ZEPRILO.COM is a premium domain sales company. Our competitors are companies like vastplots.example, getparcels.example, peerwords.example. Our current site is at www.zeprilos.example.

We want to have the ability to search for domains, to highlight special offers and have some testimonials on the index page.

The logo for the site is attached.

Please be sure that the order form fits on the screen without scrolling the page. I want the entire form, including the submit button to fit without any page scrolling.

Delivered product - INDEX PAGE, ORDER FORM AND CONTENT PAGE PSDs.

Target Market(s)

Small to Medium business professionals

Industry/Entity Type

It Company

Requirements
Must have
• 1. List of domains for sale
2. Simple search box with button to run the search
3. link for advanced search
4. testimonial area. Note - this can be a small box where a different testimonial is displayed on each page load.
Nice to have
• Would like the site to have some white space. Don't want a heavily packed website. Give it an "airy" feel.

```html
<!DOCTYPE html>
<html lang="en">
<head>
<meta charset="utf-8">
<title>ZEPRILO.COM – Premium Domains</title>
<link rel="stylesheet" href="https://fonts.googleapis.com/css2?family=Open+Sans:ital,wght@0,300;0,400;0,600;0,700;1,400&family=Norican&family=Lora:ital,wght@1,400;1,700&display=swap">
<style>
:root{
  --blue:#0c4d99;
  --green:#0a7a38;
  --green-dark:#066b30;
  --orange:#f5a000;
  --gray:#666;
  --light:#bbb;
  --ink:#222;
}
*{box-sizing:border-box;margin:0;padding:0}
html,body{width:1049px;height:1200px;overflow:hidden;background:#fff;font-family:"Open Sans",sans-serif}
.page{position:relative;width:1049px;height:1200px;overflow:hidden}
.abs{position:absolute}

.site-header{left:0;top:0;width:1049px;height:85px;background:linear-gradient(#f4f4f4,#e6e6e6)}
.brand{left:105px;top:26px;font-size:31px;font-weight:700;color:var(--blue);letter-spacing:-1px;display:flex;align-items:center;gap:6px}
.brand-dot{width:14px;height:14px;border-radius:50%;background:var(--green)}
.phone-tab{left:783px;top:0;width:161px;height:28px;background:var(--green);color:#fff;font-size:14px;font-style:italic;display:flex;align-items:center;justify-content:center;gap:6px}
.nav{left:346px;top:31px;display:flex;align-items:center;font-size:15px;font-weight:600;color:#555;height:33px}
.nav a{color:inherit;text-decoration:none;margin-right:19px;display:flex;align-items:center;gap:4px}
.nav a.active{background:var(--blue);color:#fff;padding:0 13px;height:33px;line-height:33px;margin-right:22px}
.nav .light{font-weight:400}

.hero{left:0;top:85px;width:1049px;height:440px;background:radial-gradient(ellipse at 70% 45%,#c3cdd6 0%,#7d93a8 45%,#3c5068 100%)}
.hero-people{left:50px;top:150px;width:410px;height:350px;border-radius:40% 40% 10% 10%;background:radial-gradient(ellipse at 50% 45%,#e9dccb,#a9a7b5 55%,rgba(120,130,150,0) 75%)}
.special-tab{left:0;top:184px;width:43px;height:182px;background:var(--green);color:#fff;font-size:19px;writing-mode:vertical-rl;transform:rotate(180deg);display:flex;align-items:center;justify-content:center}
.badge{left:348px;top:327px;width:86px;height:86px;border-radius:50%;background:#fff;color:var(--blue);text-align:center;font-weight:700;display:flex;flex-direction:column;align-items:center;justify-content:center;font-size:8px;line-height:1.1}
.badge b{font-size:18px}
.badge span.ribbon{background:var(--blue);color:#fff;padding:2px 6px;margin-top:3px;font-size:8px}
.headline{left:471px;top:200px;font-family:"Norican",cursive;color:#fff;font-size:50px;white-space:nowrap}
.subline{left:470px;top:268px;color:#fff;font-weight:300;font-size:21px;letter-spacing:-.5px}
.search{left:472px;top:316px;width:473px;height:69px;border:3px solid #fff;border-radius:5px;background:#f2f2f2;display:flex;overflow:hidden}
.search-input{flex:1;display:flex;align-items:center;padding-left:20px;font-size:21px;font-weight:300;color:#888}
.search-tld{width:72px;background:#dcdcdc;display:flex;align-items:center;justify-content:center;color:#888;font-size:14px;font-style:italic;font-weight:600}
.search-go{width:65px;background:var(--green);color:#fff;font-weight:700;font-size:26px;display:flex;align-items:center;justify-content:center}
.search-hint{left:470px;top:395px;font-family:"Lora",serif;font-style:italic;font-size:9px;color:#333}
.adv{left:828px;top:395px;font-size:13px;color:var(--orange);display:flex;align-items:center;gap:5px}
.adv i{width:10px;height:10px;border-radius:50%;background:var(--orange);display:inline-block}
.hero-edge{left:0;top:460px}

.script-title{font-family:"Norican",cursive;color:var(--blue);font-size:34px}
.kicker{font-size:11px;color:var(--ink);display:flex;align-items:center;gap:6px}
.kicker hr{border:0;border-top:3px double #ccc;flex:1}
.sold{left:98px;top:597px;width:303px}
.sold .kicker{margin-top:4px;padding-left:7px}
.sold-names{left:105px;top:697px;width:300px;display:flex;flex-wrap:wrap;gap:22px 30px;align-items:center;color:#aaa;font-size:22px;font-weight:600}
.sold-names span{display:flex;align-items:center;gap:6px}
.sold-names i{width:26px;height:26px;border-radius:50%;background:#c8c8c8;display:inline-block}

.testimonials{left:469px;top:597px;width:475px}
.testimonials .kicker{margin-top:4px}
.quote{top:688px;width:215px}
.quote h3{font-size:17px;font-weight:400;color:var(--blue)}
.quote h4{font-family:"Lora",serif;font-style:italic;font-weight:700;font-size:13px;color:var(--ink);margin-top:4px}
.quote p{font-family:"Lora",serif;font-style:italic;font-size:11px;line-height:13.5px;color:#555}
.quote .date{font-family:"Norican",cursive;color:var(--orange);font-size:14px;margin-top:12px;display:flex;align-items:center;gap:6px}
.quote .date b{color:#ccc;font-family:Georgia,serif;font-size:20px}

.stats{left:0;top:876px;width:1049px;height:104px;background:linear-gradient(90deg,var(--green-dark) 0%,var(--green) 70%,#3d9a3a 100%)}
.stat{top:27px;text-align:center;color:#cfe8d5;font-weight:300;font-size:31px;line-height:26px;width:200px}
.stat .tag{position:absolute;top:-27px;background:var(--orange);color:#fff;font-size:9px;font-weight:700;line-height:17px;padding:0 9px}
.sep{top:54px;width:17px;border-top:1px solid #8bc49a}

.footer-links{top:1045px;font-size:11px;color:#666;line-height:19.7px;list-style:none}
.footer-links li::before{content:"›";color:#bbb;margin-right:6px}
.call{left:416px;top:1036px;color:var(--blue);font-size:23px;line-height:28px}
.phones{left:594px;top:1043px;font-size:20px;line-height:27px;color:#777;font-style:italic;letter-spacing:-1px}
.accept{left:416px;top:1107px;font-family:"Norican",cursive;font-size:23px;color:var(--blue)}
.cards{left:551px;top:1117px;display:flex;gap:7px;font-size:8px;font-weight:700;color:#444}
.cards span{display:flex;align-items:center;gap:3px}
.cards i{width:9px;height:9px;background:#1d4f9c;display:inline-block}
.foot-brand{left:790px;top:1030px;font-size:33px;font-weight:700;color:#d3d3d3;letter-spacing:-1px}
.legal{left:793px;top:1079px;font-size:11px;color:#777;line-height:14px}
</style>
</head>
<body>
<div class="page">
  <header class="site-header abs">
    <div class="brand abs"><span class="brand-dot"></span>ZEPRILO</div>
    <div class="phone-tab abs">
      <svg width="13" height="13" viewBox="0 0 16 16"><circle cx="8" cy="8" r="7" fill="none" stroke="#fff" stroke-width="1.4"/><path d="M5.5 4.5l1.3 1.6-.8 1c.6 1.2 1.4 2 2.6 2.6l1-.8 1.6 1.3-.9 1.2c-2.9-.5-5-2.7-5.5-5.5z" fill="#fff"/></svg>
      866-555-ZEPRILO
    </div>
    <nav class="nav abs">
      <a class="active" href="#">HOME</a>
      <a href="#">CATEGORIES</a>
      <a href="#">FAQS</a>
      <a href="#">ABOUT</a>
      <a href="#">CONTACT</a>
      <a class="light" href="#"><svg width="15" height="12" viewBox="0 0 15 12"><path d="M0 1h3l2 7h8l1.5-5H4" fill="none" stroke="#666" stroke-width="1.3"/><circle cx="6" cy="10.5" r="1.2" fill="#666"/><circle cx="12" cy="10.5" r="1.2" fill="#666"/></svg>MYCART</a>
      <a class="light" href="#"><svg width="11" height="12" viewBox="0 0 11 12"><circle cx="5.5" cy="3" r="3" fill="#666"/><path d="M0 12c0-4 2-5.5 5.5-5.5S11 8 11 12z" fill="#666"/></svg>MY ACCOUNT</a>
    </nav>
  </header>

  <section class="hero abs" role="img" aria-label="Blurred server room background"></section>
  <div class="hero-people abs" role="img" aria-label="Photo of a smiling couple buying online at a laptop"></div>
  <div class="special-tab abs">Special Offer</div>
  <div class="badge abs">PREMIUM DOMAIN<b>$10</b>ONLY<span class="ribbon">SPACIAL OFFER</span></div>
  <h1 class="headline abs">Your Business Starts Here</h1>
  <p class="subline abs">BUY A PREMIUM DOMAIN AND OPEN YOUR DOORS</p>
  <form class="search abs">
    <div class="search-input">Enter your domain</div>
    <div class="search-tld">.COM ▾</div>
    <div class="search-go">GO</div>
  </form>
  <p class="search-hint abs">Start your search by entering the first character of the domain name.</p>
  <a class="adv abs">Advanced Search <i></i></a>
  <svg class="hero-edge abs" width="1049" height="70" viewBox="0 0 1049 70">
    <polygon points="0,46 1049,10 1049,24 0,60" fill="#2a2a2a"/>
    <polygon points="0,60 1049,24 1049,70 0,70" fill="#fff"/>
  </svg>

  <section class="sold abs">
    <h2 class="script-title">Domain Sold</h2>
    <div class="kicker">MISSED GIVEN BELOW DOMAIN <hr></div>
  </section>
  <div class="sold-names abs">
    <span><i></i>Norvale</span>
    <span>Travique</span>
    <span style="font-size:15px">Zentro</span>
    <span style="font-size:15px">Brixfield</span>
    <span style="font-size:17px">Orland Life</span>
  </div>

  <section class="testimonials abs">
    <h2 class="script-title">Testimonials</h2>
    <div class="kicker">WHAT PEOPLE ARE SAYING ABOUT US. <hr></div>
  </section>
  <article class="quote abs" style="left:470px">
    <h3>getparcels.example</h3>
    <h4>Maren - United Kingdom</h4>
    <p>Lorem ipsum dolor sit amet, consectetur adipisicing elit, sed do eiusmod incididunt dolor sit amet dolor amet</p>
    <div class="date"><b>“</b>June 15, 2011, 3p.m</div>
  </article>
  <article class="quote abs" style="left:731px">
    <h3>getparcels.example</h3>
    <h4>Maren - United Kingdom</h4>
    <p>Lorem ipsum dolor sit amet, consectetur adipisicing elit, sed do eiusmod incididunt dolor sit amet dolor amet</p>
    <div class="date"><b>“</b>June 15, 2011, 3p.m</div>
  </article>

  <section class="stats abs">
    <div class="stat abs" style="left:56px"><span class="tag" style="left:83px">OVER</span>350,000<br>Domains</div>
    <div class="sep abs" style="left:265px"></div>
    <div class="stat abs" style="left:298px"><span class="tag" style="left:77px">100%</span>Satisfaction<br>Guarantee</div>
    <div class="sep abs" style="left:513px"></div>
    <div class="stat abs" style="left:535px">World Class<br>Guarantee</div>
    <div class="sep abs" style="left:752px"></div>
    <div class="stat abs" style="left:773px">Trusted<br>And Secure</div>
  </section>

  <ul class="footer-links abs" style="left:107px">
    <li>Home</li><li>Categories</li><li>Faq's</li><li>About Us</li><li>Contact Us</li>
  </ul>
  <ul class="footer-links abs" style="left:223px">
    <li>Traffic Score</li><li>Domain Rank</li><li>Popularity Score</li><li>US Based Traffic Percent</li><li>Testimonials</li>
  </ul>
  <p class="call abs">Call Our Domain<br>Experts Today</p>
  <p class="phones abs">866-555-ZEPRILO<br>866-555-ZEPRIL2</p>
  <p class="accept abs">We Accept</p>
  <div class="cards abs">
    <span><i></i>Payvia</span><span>Cardmix</span><span>Amberpay</span><span>Findcard</span><span>Tablepay</span>
  </div>
  <div class="foot-brand abs">ZEPRILO</div>
  <p class="legal abs">All Right Reseved © 2013<br>Privacy Policy &nbsp;| &nbsp;Terms</p>
</div>
</body>
</html>
```